Sale of South Sea and Tahitian Pearl Jewellery, online business

I need a business card designed for my website business. We sell South Sea and Tahitian Pearl Jewellery. The colour theme for the website is black and white and would like to carry this through to business cards. Our brand is very elegant and stylish, would like sketch picture of women or fashion involving pearls if not the sketched picture then have the card very plan. below are pictures of the ideas I like and also the logo and writing that is used on my jewellery boxes.
Font is English Hand DB

Target Market(s)

30 and over women in the high end of the market

Industry/Entity Type

Business

Contact Information for Business Card

Business name - Varno Gems( front of card)
Back of card -Details
Corinne Mabbutt
Gemmologist FGAA
email: corinne@varnogems.com.au
website: varnogems.com.au
mob: +61 427 806 193
Perth Australia

Varno Orbix PTY T/AS Varno Gems
ABN 72 384 516 907

Colors
1b1b1b
ffffff
85cae6

Requirements
Must have
• Black and white colour preferably black card with white writing and picture.
• The Same writing as logo and writing on box packaging, attached a file with writing.
• Business name on one side of the card and all other details on the other side.
• Can have tiny hints of the tiffany blue colour.
• Font: English Hand DB
Nice to have
• I really like the idea of having a sketch of a stylish or elegent lady wearing pearls or a sketch of a pearl, if not the sketch a really plain and simple card.
Should not have
• busy patterns.

```html
<!DOCTYPE html>
<html lang="en">
<head>
<meta charset="utf-8">
<title>Varno Gems — Business Card</title>
<link rel="stylesheet" href="https://fonts.googleapis.com/css2?family=Pinyon+Script&family=Arimo:wght@400;700&display=swap">
<style>
  :root {
    --stage-dark: #3c3c3c;
    --stage-light: #5e5e5e;
    --card-white: #ffffff;
    --card-black: #000000;
    --ink: #1b1b1b;
    --tiffany: #85cae6;
    --tiffany-soft: #e6f4fa;
  }
  * { margin: 0; padding: 0; box-sizing: border-box; }
  html, body { width: 999px; height: 1200px; overflow: hidden; }
  body {
    position: relative;
    background: radial-gradient(ellipse at center, var(--stage-light) 0%, var(--stage-dark) 100%);
    font-family: "Arimo", Arial, sans-serif;
    color: var(--ink);
  }
  .card {
    position: absolute;
    left: 57px;
    width: 898px;
    height: 513px;
  }
  .card--front { top: 91px; background: var(--card-white); }
  .card--back { top: 637px; background: var(--card-black); }

  .holder-name {
    position: absolute;
    left: 33px; top: 50px;
    font-family: "Pinyon Script", cursive;
    font-size: 46px;
    line-height: 1;
    color: var(--card-black);
  }
  .holder-title {
    position: absolute;
    left: 32px; top: 122px;
    font-size: 21px;
  }
  .contact-list {
    position: absolute;
    left: 32px; top: 234px;
    list-style: none;
  }
  .contact-list li {
    display: flex;
    align-items: center;
    height: 30px;
    font-size: 21px;
  }
  .contact-list svg {
    width: 16px; height: 16px;
    margin-right: 21px;
    flex: none;
  }
  .location {
    position: absolute;
    left: 32px; top: 372px;
    font-size: 21px;
    font-weight: 700;
  }
  .company {
    position: absolute;
    left: 32px; top: 432px;
    font-size: 21px;
    line-height: 30px;
  }
  .company strong { font-weight: 700; }
  .fashion-sketch {
    position: absolute;
    left: 640px; top: 30px;
    width: 255px; height: 470px;
    background: linear-gradient(180deg, #ffffff 0%, var(--tiffany-soft) 45%, #ffffff 100%);
    border-radius: 6px;
  }

  .brand-ring {
    position: absolute;
    left: 343px; top: 113px;
    width: 210px; height: 210px;
    border: 3px solid var(--card-white);
    border-radius: 50%;
  }
  .brand-name {
    position: absolute;
    left: 0; right: 0; top: 322px;
    text-align: center;
    font-family: "Pinyon Script", cursive;
    font-size: 72px;
    line-height: 1;
    color: var(--card-white);
  }
</style>
</head>
<body>
  <section class="card card--front">
    <h1 class="holder-name">Corinne Mabbutt</h1>
    <p class="holder-title">Gemmologist FGAA</p>
    <ul class="contact-list">
      <li>
        <svg viewBox="0 0 16 16" aria-hidden="true"><rect x="3.5" y="1" width="9" height="14" rx="1.5" fill="none" stroke="#1b1b1b" stroke-width="2"/><line x1="6.5" y1="4" x2="9.5" y2="4" stroke="#1b1b1b" stroke-width="1.5"/></svg>
        +61 427 806 193
      </li>
      <li>
        <svg viewBox="0 0 16 16" aria-hidden="true"><path d="M1 6 L8 1.5 L15 6 V14.5 H1 Z" fill="#1b1b1b"/><path d="M3 7 L8 10.5 L13 7" fill="none" stroke="#fff" stroke-width="1.3"/></svg>
        corinne@varnogems.com.au
      </li>
      <li>
        <svg viewBox="0 0 16 16" aria-hidden="true"><g fill="none" stroke="#1b1b1b" stroke-width="1"><circle cx="8" cy="8" r="7"/><ellipse cx="8" cy="8" rx="3" ry="7"/><line x1="1" y1="8" x2="15" y2="8"/><line x1="8" y1="1" x2="8" y2="15"/><path d="M2.5 4.5 H13.5 M2.5 11.5 H13.5"/></g></svg>
        varnogems.com.au
      </li>
    </ul>
    <p class="location">Perth Australia</p>
    <p class="company">Varno Orbix PTY T/AS Varno Gems<br><strong>ABN</strong> 72 384 516 907</p>
    <div class="fashion-sketch" role="img" aria-label="Line sketch of an elegant woman in sunglasses and a pale blue dress walking with a handbag"></div>
  </section>

  <section class="card card--back">
    <div class="brand-ring" aria-hidden="true"></div>
    <p class="brand-name">Varno Gems</p>
  </section>
</body>
</html>
```